Zestra Design Prize - $10,000 tablet app design contest, Event App Category

Zestra is a marketplace for Kelo App Templates (similar to PageLoom templates). We want you to design an app template for sale in our marketplace which targets Event Apps (Kelo Apps that are created around music festivals, tradeshows, conferences or other events).

It’s up to you to create pages or features for the App Template that you think are appropriate. Creativity will be rewarded! Here are some example pages or features that you could create:

• A welcome page
• Event details – when and where?
• A location map
• A contact details page
• An event calendar (what’s on when?)
• Social media integration
• Video or animations

Your design should be Vibrant, Engaging and Contemporary. If you have an Kelo, download Zestra Viewer and download template examples in the download tab.

Your entry must include:
• A brief description of your template
• preview images of all pages of your template

Attached to this project are free templates to help you get started with your design. We have included:
1. A free portfolio template for designers/photographers
2. Icons and artwork to use in your template
3. Blank pages template
4. Form template
5. Video ad template

If you are selected as a finalist you will be required to submit an .oproject file containing:
• Your InDesign source files
• Preview images of your template
• All creative / stock assets used in the template (animations, video etc.)
• A text file with instructions on how to update the template
• A metadata .txt file containing template details and your information

How to enter:
1. Register at Marketplace and view the instructions under the welcome message https://marketplace.zestrahq.example/welcome
2. Download Zestra Editor: https://support.zestrahq.example/entries/58104963-zestra-editor
3. Use the free templates provided in this brief to create your designs and submit to ArtHively

Reason: Due to the Christmas break we are extending the deadline of our competition. Thank you for time and effort - I will be providing feedback over the next couple of days! Best wishes, Mirela

Hi All,

I have received many screenshots with some great designs! I just wanted to clarify that you are designing Zestra app templates including Zestra features and not just page designs?

Read Tips for First Time Zestrans to guide you through the template creation process

Before you start designing templates for Zestra Marketplace

·       Read the Quality Standards

·       Read the Copyright Information 

·       Use the Template Quality Checklist to ensure your template follows our guidelines. 

What should my project file contain?

·       A folder containing your source files, e.g. InDesign. This must be named Source.

·       The Zestra content files. This must be named Bundle.

·       Instructions, explaining to a customer how to use your template.

Best wishes,

Mirela

Reason: We are extending the competition by 7 days to give you more time!

Reason: Hello - we have received 3 entries for this contest so we are extending the deadline by 7 days. Best wishes, Mirela :)

Target Market(s)

Entrepreneurs who wish to create Kelo Apps by using our App design templates.

Industry/Entity Type

Events

Requirements
Must have
• You will need Zestra Editor to open the .oproject files attached to this brief. Get it here: https://support.zestrahq.example/entries/58104963-zestra-editor
Should not have
• Low quality, fuzzy or blurry images
- Any stock images or content which you do not own the rights to
- Any material which could be considered inappropriate or offensive

```html
<!DOCTYPE html>
<html lang="en">
<head>
<meta charset="utf-8">
<title>Event List</title>
<link rel="stylesheet" href="https://fonts.googleapis.com/css2?family=Roboto+Condensed:wght@700&family=Yesteryear&family=Quicksand:wght@500&family=Lato:wght@400;700&display=swap">
<style>
  :root {
    --bar-black: #000000;
    --status-text: #d9d9d9;
    --amber: #fdbf00;
    --amber-light: #ffd226;
    --amber-edge: #d99e00;
    --nav-text: #5a3a00;
    --paper: #efedea;
    --ink: #111111;
    --rule: #1d2233;
    --shadow: rgba(90, 85, 80, 0.45);
    --toolbar-top: #b9c3c0;
    --toolbar-bottom: #67706d;
  }
  * { box-sizing: border-box; margin: 0; padding: 0; }
  html, body { width: 948px; height: 1200px; overflow: hidden; background: var(--paper); }
  .screen { position: relative; width: 948px; height: 1200px; background: var(--paper); font-family: "Lato", sans-serif; color: var(--ink); }

  .status-bar { position: absolute; top: 0; left: 0; width: 948px; height: 33px; background: var(--bar-black); color: var(--status-text); font: 700 19px "Lato", sans-serif; }
  .status-bar .carrier { position: absolute; left: 6px; top: 5px; display: flex; align-items: center; gap: 8px; }
  .status-bar .clock { position: absolute; left: 0; right: 0; top: 5px; text-align: center; }
  .status-bar .indicators { position: absolute; right: 6px; top: 8px; display: flex; gap: 12px; align-items: center; }

  .main-nav { position: absolute; top: 33px; left: 0; width: 948px; height: 59px; display: flex; background: var(--amber); }
  .main-nav a { display: flex; align-items: center; justify-content: center; height: 100%; border-right: 2px solid var(--amber-edge); color: var(--nav-text); text-decoration: none; font: 700 19px "Roboto Condensed", sans-serif; background: linear-gradient(var(--amber-light), var(--amber)); }
  .main-nav a:last-child { border-right: none; }

  .page-title { position: absolute; left: 32px; top: 124px; font: 400 60px "Yesteryear", cursive; color: var(--ink); }
  .title-rule { position: absolute; left: 30px; top: 201px; width: 880px; height: 2px; background: var(--rule); }

  .session { position: absolute; left: 37px; font-size: 16px; display: flex; }
  .session .time { width: 326px; font-weight: 700; }
  .session .speaker { letter-spacing: 0.3px; }

  .section-shadow { position: absolute; left: 90px; width: 830px; height: 22px; background: radial-gradient(ellipse at 55% 100%, var(--shadow), transparent 70%); }

  .break-banner { position: absolute; left: 30px; width: 567px; height: 62px; background: var(--amber); clip-path: polygon(0 0, 93% 0, 100% 100%, 0 100%); display: flex; align-items: center; padding-left: 11px; font: 500 29px "Quicksand", sans-serif; color: var(--ink); }

  .scroll-hint { position: absolute; left: 883px; top: 1090px; }

  .toolbar { position: absolute; left: 0; top: 1131px; width: 948px; height: 69px; background: var(--bar-black); }
  .toolbar .strip { height: 36px; background: linear-gradient(var(--toolbar-top), var(--toolbar-bottom)); border-top: 1px solid #8a928f; }
  .next-button { position: absolute; left: 880px; top: 20px; }
</style>
</head>
<body>
<div class="screen">
  <header class="status-bar">
    <div class="carrier">Kelo
      <svg width="24" height="18" viewBox="0 0 24 18"><path d="M2 7a14 14 0 0 1 20 0M5.5 10.5a9 9 0 0 1 13 0M9 14a4 4 0 0 1 6 0" fill="none" stroke="#d9d9d9" stroke-width="2.6" stroke-linecap="round"/></svg>
    </div>
    <div class="clock">4:20 PM</div>
    <div class="indicators">
      <svg width="16" height="16" viewBox="0 0 16 16"><circle cx="8" cy="8" r="7" fill="#d9d9d9"/><path d="M8 4v4h3" stroke="#000" stroke-width="1.8" fill="none"/></svg>
      <svg width="34" height="16" viewBox="0 0 34 16"><rect x="1" y="1" width="29" height="14" fill="none" stroke="#d9d9d9" stroke-width="2"/><rect x="4" y="4" width="23" height="8" fill="#d9d9d9"/><rect x="31" y="5" width="3" height="6" fill="#d9d9d9"/></svg>
    </div>
  </header>

  <nav class="main-nav">
    <a href="#" style="width:139px">Welcome</a>
    <a href="#" style="width:177px">Event Details</a>
    <a href="#" style="width:194px">Event Calendar</a>
    <a href="#" style="width:143px">Location</a>
    <a href="#" style="width:136px">Contact</a>
    <a href="#" style="width:159px">Get In touch</a>
  </nav>

  <h1 class="page-title">Event List</h1>
  <div class="title-rule"></div>

  <div class="session" style="top:236px"><span class="time">8:30 AM – 9:30 AM</span><span class="speaker">Lorem ipsum dolor sit amet.</span></div>
  <div class="session" style="top:271px"><span class="time">9:30 AM – 10:00 AM</span><span class="speaker">Navo Velandra</span></div>
  <div class="session" style="top:306px"><span class="time">10:00AM – 11: AM</span><span class="speaker">Esta Di Marlo</span></div>
  <div class="section-shadow" style="top:318px"></div>
  <div class="break-banner" style="top:350px">COFFEE BREAK 11.00 AM - 11.45 AM</div>

  <div class="session" style="top:467px"><span class="time">12.00 AM – 1:00 PM</span><span class="speaker">Lorem ipsum dolor sit amet &amp; Navo Velandra</span></div>
  <div class="section-shadow" style="top:551px"></div>
  <div class="break-banner" style="top:580px">LUNCH BREAK 1:00 PM - 2:00 PM</div>

  <div class="session" style="top:698px"><span class="time">2.00 PM – 3:00 PM</span><span class="speaker">Lorem ipsum dolor sit amet</span></div>
  <div class="session" style="top:733px"><span class="time">3:00 PM – 4:30 PM</span><span class="speaker">Navo Velandra</span></div>
  <div class="section-shadow" style="top:782px"></div>
  <div class="break-banner" style="top:812px">TEA BREAK 4:30 PM - 5:00 PM</div>

  <div class="session" style="top:928px"><span class="time">2.00 PM – 3:00 PM</span><span class="speaker">Lorem ipsum dolor sit amet</span></div>
  <div class="session" style="top:963px"><span class="time">3:00 PM – 4:30 PM</span><span class="speaker">Navo Velandra</span></div>
  <div class="section-shadow" style="top:1012px"></div>
  <div class="break-banner" style="top:1042px">TEA BREAK 4:30 PM - 5:00 PM</div>

  <svg class="scroll-hint" width="28" height="32" viewBox="0 0 28 32" aria-label="Scroll down"><path d="M9 0h10v16h8L14 31 1 16h8z" fill="#111"/></svg>

  <footer class="toolbar">
    <div class="strip"></div>
    <svg class="next-button" width="40" height="38" viewBox="0 0 40 38" aria-label="Next"><rect x="1" y="1" width="38" height="36" rx="3" fill="#e8a000" stroke="#8a5a00" stroke-width="2"/><path d="M15 9l11 10-11 10" fill="none" stroke="#1a1000" stroke-width="4"/></svg>
  </footer>
</div>
</body>
</html>
```